43 Year Old Construction firm needs Updated Business Card & Stationery Design

We are an established and well known (in our market) commercial construction firm. We need a cleaner and more modern look for our corporate identity material. We would like to continue to use our current colors and logo.
We are thinking about incorporating a slogan on our business card (either front or back): "Striving to be the most trusted builder in our market." The text could change at some point. Our website is www.kradworth.example . Sample card is attached. Some will have more phone numbers, etc...
Updates

Target Market(s)

Commercial and institutional clients.

Industry/Entity Type

Construction Company

Contact Information for Business Card

See attached for existing card. But don't be constrained.

Requirements
Must have
• Logo, name, title, address, website, email, phone numbers (as few as one, as many as three)
• Slogan on front or back "Striving to be the most trusted builder in our market"
• Use existing logo and colors

```html
<!DOCTYPE html>
<html lang="en">
<head>
<meta charset="utf-8">
<title>Kradworth Constructors — Stationery</title>
<link href="https://fonts.googleapis.com/css2?family=Crimson+Pro:wght@400;600&family=PT+Sans:wght@400&display=swap" rel="stylesheet">
<style>
  :root{
    --backdrop:#5a5b59;
    --paper-light:#f5f5f5;
    --paper-dark:#e3e3e3;
    --brand-blue:#004a87;
    --brand-green:#179a4d;
    --ink:#4a4a4a;
    --ink-soft:#5b5b5b;
    --white:#ffffff;
  }
  *{margin:0;padding:0;box-sizing:border-box}
  html,body{width:1200px;height:793px;overflow:hidden;background:var(--backdrop)}
  .canvas{position:relative;width:1200px;height:793px}
  .sheet{position:absolute;background:linear-gradient(120deg,var(--paper-light) 0%,var(--paper-dark) 70%);box-shadow:0 1px 3px rgba(0,0,0,.35)}

  /* logo block */
  .logo-block{position:absolute;background:var(--brand-blue);color:var(--white);display:flex;flex-direction:column;align-items:center;justify-content:flex-end;padding-bottom:8px;font-family:"Crimson Pro",Georgia,serif;font-weight:600;line-height:1}
  .logo-block .name{font-size:17px;letter-spacing:.5px}
  .logo-block .sub{font-size:8.5px;letter-spacing:1px;margin-top:5px}

  /* letterhead */
  .letterhead{left:44px;top:34px;width:515px;height:725px}
  .letterhead .logo-block{left:50px;top:0;width:101px;height:90px}
  .salutation{position:absolute;left:46px;top:203px;font-family:"PT Sans",Arial,sans-serif;font-size:13.5px;color:var(--ink)}
  .letter-body{position:absolute;left:46px;top:278px;width:414px;font-family:"PT Sans",Arial,sans-serif;font-size:7.6px;line-height:12.4px;color:var(--ink);text-align:justify}
  .letter-body p{margin-bottom:12.4px}
  .closing{position:absolute;left:46px;top:504px;font-family:"PT Sans",Arial,sans-serif;font-size:7.6px;color:var(--ink)}
  .signature{position:absolute;left:44px;top:522px;width:70px;height:30px;background:linear-gradient(90deg,rgba(60,60,70,.18),rgba(60,60,70,.06));border-radius:2px}
  .signer-name{position:absolute;left:46px;top:553px;font-family:"Crimson Pro",Georgia,serif;font-size:11px;font-variant:small-caps;letter-spacing:.4px;color:var(--brand-blue)}
  .signer-title{position:absolute;left:46px;top:566px;font-family:"Crimson Pro",Georgia,serif;font-size:8px;font-variant:small-caps;letter-spacing:.3px;color:var(--brand-green)}
  .letter-contact{position:absolute;left:48px;top:640px;font-family:"Crimson Pro",Georgia,serif;font-size:9px;color:var(--ink-soft);line-height:11.5px}
  .contact-line{display:flex;align-items:center;gap:5px;margin-top:2px}
  .contact-line svg{width:9px;height:9px;flex:none}
  .contact-address{margin-bottom:4px}

  /* envelope back */
  .envelope-back{left:575px;top:206px;width:578px;height:262px}
  .envelope-back .flap{position:absolute;left:0;top:0;width:578px;height:100px}
  .flap-mark{position:absolute;left:0;width:578px;top:30px;text-align:center;color:var(--white);font-family:"Crimson Pro",Georgia,serif;font-weight:600;line-height:1}
  .flap-mark .name{display:block;font-size:20px;letter-spacing:.6px}
  .flap-mark .sub{display:block;font-size:8.5px;letter-spacing:1px;margin-top:6px}

  /* envelope front */
  .envelope-front{left:577px;top:495px;width:580px;height:262px}
  .envelope-front .logo-block{left:19px;top:0;width:100px;height:71px;padding-bottom:6px}
  .envelope-front .logo-block .name{font-size:15px}
  .envelope-front .logo-block .sub{font-size:7.5px;margin-top:4px}
  .return-address{position:absolute;left:19px;top:72px;width:100px;text-align:center;font-family:"Crimson Pro",Georgia,serif;font-size:8.8px;line-height:11.5px;color:var(--ink-soft)}
</style>
</head>
<body>
<main class="canvas">

  <section class="sheet letterhead" aria-label="Letterhead">
    <div class="logo-block"><span class="name">KRADWORTH</span><span class="sub">CONSTRUCTORS</span></div>

    <p class="salutation">Dear Mr. Ellison,</p>

    <div class="letter-body">
      <p>Lorem ipsum dolor sit amet, consectetur adipiscing elit. Donec orci purus, luctus vitae dignissim eu, iaculis sed purus. Vivamus faucibus, ipsum nec aliquet viverra, leo mauris condimentum ligula, sit amet sagittis enim ligula quis arcu. Nam egestas tortor id nisi porttitor mattis. In tortor ante, ultricies in suscipit a, tempus non massa. Vivamus et auctor mi. Fusce vel massa nulla. Phasellus nec eros mauris, et scelerisque orci.</p>
      <p>Donec malesuada orci vitae nulla accumsan porta a id massa. Quisque accumsan iaculis magna sit amet fringilla. Maecenas consequat, magna eget tincidunt semper, odio nibh rutrum mi, id feugiat ante nisi eu risus. Vestibulum nunc orci, rhoncus a placerat in, ultricies in mi. Cras mattis varius eros, vel fringilla nisi suscipit eget. Quisque scelerisque sagittis nulla at porttitor.</p>
      <p>Sed id augue vitae urna euismod commodo aliquet a quam. Pellentesque arcu velit, cursus et malesuada ut, consequat et diam. Nullam erat sem, rhoncus id ullamcorper vitae, rhoncus et arcu. In ultricies ultricies nulla, ut rutrum nisi iaculis at. Donec eu magna a metus ornare faucibus. Fusce aliquet faucibus ultricies. Morbi semper, est id tincidunt gravida, sem arcu adipiscing lacus, ac bibendum nulla leo eu purus. Quisque nec diam sed risus consectetur a accumsan quis quis nibh. Vestibulum id purus lorem.</p>
      <p>It is a long established fact that a reader will be distracted by the readable content of a page when looking at its layout. The point of using Lorem Ipsum is that it has a more-or-less normal distribution of letters, as opposed to using 'Content here, content here', making it look like readable English. Many desktop publishing packages</p>
    </div>

    <p class="closing">Sincerely,</p>
    <div class="signature" role="img" aria-label="Handwritten signature"></div>
    <p class="signer-name">Daniel Harrow</p>
    <p class="signer-title">CEO/Founder</p>

    <address class="letter-contact" style="font-style:normal">
      <div class="contact-address">4820 larkspur avenue<br>fenwick, MO 63190</div>
      <div class="contact-line">
        <svg viewBox="0 0 10 10"><path d="M2 .8 3.6 2.6 2.8 3.8c.6 1.4 1.9 2.7 3.3 3.3l1.2-.8L9.1 8 8 9.3C4.2 9 1 5.8.7 2Z" fill="var(--brand-blue)"/></svg>
        <span>555.014.2290</span>
      </div>
      <div class="contact-line">
        <svg viewBox="0 0 10 10"><rect x=".5" y="2" width="9" height="6.2" fill="var(--brand-blue)"/><path d="M.8 2.3 5 5.6l4.2-3.3" fill="none" stroke="var(--white)" stroke-width=".8"/></svg>
        <span>name@kradworth.example</span>
      </div>
      <div class="contact-line">
        <svg viewBox="0 0 10 10"><circle cx="5" cy="5" r="4.5" fill="var(--brand-blue)"/><path d="M.5 5h9M5 .5c-2 2.5-2 6.5 0 9M5 .5c2 2.5 2 6.5 0 9" fill="none" stroke="var(--white)" stroke-width=".6"/></svg>
        <span>www.kradworth.example</span>
      </div>
    </address>
  </section>

  <section class="sheet envelope-back" aria-label="Envelope back">
    <svg class="flap" viewBox="0 0 578 100" aria-hidden="true">
      <path d="M0 0H578L568 58Q562 96 522 96H52Q18 96 11 58Z" fill="#d9e1e4"/>
      <path d="M0 0H578L568 56Q561 93 522 93H52Q18 93 11 56Z" fill="var(--brand-blue)"/>
    </svg>
    <div class="flap-mark"><span class="name">KRADWORTH</span><span class="sub">CONSTRUCTORS</span></div>
  </section>

  <section class="sheet envelope-front" aria-label="Envelope front">
    <div class="logo-block"><span class="name">KRADWORTH</span><span class="sub">CONSTRUCTORS</span></div>
    <address class="return-address" style="font-style:normal">4820 larkspur avenue<br>fenwick, MO 63190</address>
  </section>

</main>
</body>
</html>
```